Pricing sheet For Acupuncture Clinic - Remake Attached Work

Right Now I have 4 pricing sheets that look very disorganized. They are for 4 different options of services I offer with 3 different options to pay for each service (pay each time you come in, prepaid package, or a monthly option). People get confused from this outline so looking to make this easier to understand and better looking. You can reorganize the pricing as you see fit as long as it makes sense. (ex: using columns or rows or a graph) These images are going to be made into standard sized posters (i think that is 5 feet by 7 feet?)

Instead of designing all 4 of the attached files below you can choose 1 of them to show your example of work. I will assume that style will apply to all 4 sheets if I choose your work - also need 1 sheet that can print out on paper that will show all treatments on front and back of paper.

Thank you
Milo

Target Market(s)

Spa Industry

Industry/Entity Type

Clinic

Font styles to use
Serif
Sans Serif
Decorative
Script

Colors
33a6d7
ffffff
000000

Requirements
Nice to have
• clean - organized -
Should not have
• pictures of acupuncture needles. anything sharp. anything that might make people feel afraid of getting the treatments or look painful

```html
<!DOCTYPE html>
<html lang="en">
<head>
<meta charset="utf-8">
<title>Body Acupuncture Pricing</title>
<link href="https://fonts.googleapis.com/css2?family=Oswald:wght@400;500;600;700&family=Open+Sans:wght@600;700;800&display=swap" rel="stylesheet">
<style>
:root{
  --charcoal:#2e2f31;
  --charcoal-dark:#232426;
  --blue:#33a6d7;
  --blue-mid:#2a8fbf;
  --blue-deep:#1f6f99;
  --navy:#184f6f;
  --white:#ffffff;
  --ink:#000000;
  --grey:#9aa0a6;
}
*{margin:0;padding:0;box-sizing:border-box}
html,body{width:707px;height:1200px;overflow:hidden;background:var(--white)}
.sheet{width:707px;height:1200px;display:flex;flex-direction:column;font-family:'Oswald',sans-serif;color:var(--white)}
.top{background:radial-gradient(ellipse at 50% 30%,#3b3c3f 0%,var(--charcoal) 55%,var(--charcoal-dark) 100%);height:620px;position:relative;text-align:center}
.brand{position:absolute;left:50%;top:0;transform:translateX(-50%);width:150px;height:112px;background:var(--white);display:flex;align-items:center;justify-content:center;flex-direction:column;gap:6px;padding:10px}
.brand-mark{width:14px;height:14px;background:var(--blue)}
.brand-name{font-family:'Oswald',sans-serif;font-weight:600;font-size:16px;line-height:1.1;color:var(--blue);text-transform:uppercase;letter-spacing:.5px}
.title{position:absolute;top:138px;width:100%;font-weight:600;font-size:66px;letter-spacing:2px;line-height:1}
.conditions{position:absolute;top:240px;left:0;right:0;display:flex;justify-content:center;gap:26px}
.condition{display:flex;flex-direction:column;align-items:center;width:76px}
.condition-icon{width:66px;height:66px;border-radius:50%;background:var(--blue);border:3px solid #4fb7e3}
.condition-label{margin-top:8px;font-family:'Open Sans',sans-serif;font-weight:700;font-size:11px;text-transform:uppercase;line-height:1.15}
.banner{height:48px;display:flex;align-items:center;justify-content:center;font-weight:600;font-size:28px;letter-spacing:1px;text-transform:uppercase}
.banner.payg{position:absolute;top:372px;left:0;right:0;background:var(--blue)}
.retail-table{position:absolute;top:448px;left:90px;right:90px;border:2px solid var(--white)}
.retail-row{display:flex;height:56px;align-items:center}
.retail-row+.retail-row{border-top:2px solid var(--white)}
.retail-label{width:180px;text-align:right;padding-right:22px;font-family:'Open Sans',sans-serif;font-weight:800;font-size:16px;height:100%;display:flex;align-items:center;justify-content:flex-end;border-right:2px solid var(--white)}
.retail-price{padding-left:26px;font-size:34px;font-weight:600;display:flex;align-items:baseline;gap:6px}
.retail-price small{font-size:18px;font-weight:500}
.struck{position:relative;color:var(--white)}
.struck::after{content:"";position:absolute;left:-6px;right:-6px;top:50%;height:3px;background:var(--blue);transform:rotate(-18deg)}
.retail-row.ours .retail-price span:first-child{color:var(--blue)}
.prepaid{background:var(--blue);height:250px;padding-top:0}
.banner.dark{background:var(--charcoal)}
.monthly{background:linear-gradient(180deg,var(--blue-deep),var(--navy));height:252px}
.banner.navy{background:#123d56;height:44px}
.note{text-align:center;font-family:'Open Sans',sans-serif;font-weight:700;font-size:11px;margin:10px 0 8px;letter-spacing:.3px}
.rows{padding:16px 70px 0}
.monthly .rows{padding-top:0}
.row{display:flex;border:2px solid var(--white);height:52px;align-items:center}
.row+.row{margin-top:10px}
.row-label{flex:1;padding-left:20px;font-family:'Open Sans',sans-serif;font-weight:800;font-size:16px;text-transform:uppercase}
.row-label b{font-size:20px;margin-right:8px}
.row-price{width:190px;height:100%;border-left:2px solid var(--white);display:flex;align-items:center;justify-content:center;font-size:36px;font-weight:600;background:rgba(0,0,0,.12)}
.footer{flex:1;background:var(--white);color:var(--ink);display:flex;align-items:center;justify-content:center;padding:0 60px;text-align:center;font-family:'Open Sans',sans-serif;font-weight:700;font-size:11px;line-height:1.5;text-transform:uppercase;color:#444}
</style>
</head>
<body>
<div class="sheet">
  <section class="top">
    <div class="brand">
      <span class="brand-mark"></span>
      <span class="brand-name">Harbor Glow<br>Acupuncture</span>
    </div>
    <h1 class="title">BODY ACUPUNCTURE</h1>
    <ul class="conditions" style="list-style:none">
      <li class="condition"><div class="condition-icon" role="img" aria-label="Pain icon"></div><span class="condition-label">Pain</span></li>
      <li class="condition"><div class="condition-icon" role="img" aria-label="Weight loss icon"></div><span class="condition-label">Weight<br>Loss</span></li>
      <li class="condition"><div class="condition-icon" role="img" aria-label="Hormones icon"></div><span class="condition-label">Hormones</span></li>
      <li class="condition"><div class="condition-icon" role="img" aria-label="Anxiety icon"></div><span class="condition-label">Anxiety</span></li>
      <li class="condition"><div class="condition-icon" role="img" aria-label="Insomnia icon"></div><span class="condition-label">Insomnia</span></li>
      <li class="condition"><div class="condition-icon" role="img" aria-label="Allergies icon"></div><span class="condition-label">Allergies</span></li>
    </ul>
    <h2 class="banner payg">Pay As You Go</h2>
    <div class="retail-table">
      <div class="retail-row"><div class="retail-label">RETAIL:</div><div class="retail-price"><span class="struck">$75</span><small>/TREATMENT</small></div></div>
      <div class="retail-row ours"><div class="retail-label">OUR PRICE:</div><div class="retail-price"><span>$50</span><small>/TREATMENT</small></div></div>
    </div>
  </section>

  <section class="prepaid">
    <h2 class="banner dark">Pre-Paid Packages</h2>
    <div class="rows">
      <div class="row"><div class="row-label"><b>6</b>Treatments</div><div class="row-price">$270</div></div>
      <div class="row"><div class="row-label"><b>10</b>Treatments</div><div class="row-price">$480</div></div>
      <div class="row"><div class="row-label"><b>15</b>Treatments</div><div class="row-price">$720</div></div>
    </div>
  </section>

  <section class="monthly">
    <h2 class="banner navy">Monthly Auto Pay</h2>
    <p class="note">UNUSED TREATMENTS ROLL OVER · MINIMUM 4 MONTHS</p>
    <div class="rows">
      <div class="row"><div class="row-label"><b>4</b>Treatments/Month</div><div class="row-price">$160</div></div>
      <div class="row"><div class="row-label"><b>8</b>Treatments/Month</div><div class="row-price">$240</div></div>
      <div class="row"><div class="row-label"><b>12</b>Treatments/Month</div><div class="row-price">$336</div></div>
    </div>
  </section>

  <footer class="footer">
    <p>Autopay can be cancelled anytime after 4 months. Unused treatments will be forfeited 3 months after cancellation of the plan.</p>
  </footer>
</div>
</body>
</html>
```